Business card for a new cabinet shop company named Torvane Cabinets for high end cabinets

Design a business card, thinking dark rich green with colours to speak of high end luxury ie; cream, gold, black possibly

Miles Harwick
Director Craftsman
Email: info@torvanecabinets.com.au
Instagram : @torvane.cabinets

```html
<!DOCTYPE html>
<html lang="en">
<head>
<meta charset="utf-8">
<title>Torvane Cabinets – Business Card</title>
<link rel="stylesheet" href="https://fonts.googleapis.com/css2?family=Poppins:wght@400;500;700&display=swap">
<style>
  :root {
    --backdrop: #1d1d1d;
    --card-dark: #050505;
    --card-light: #ffffff;
    --gold: #c6a35a;
    --ink: #111111;
    --frame-on-dark: #f2f2f2;
    --frame-on-light: #111111;
  }
  * { margin: 0; padding: 0; box-sizing: border-box; }
  html, body {
    width: 1200px;
    height: 1200px;
    overflow: hidden;
    background: var(--backdrop);
    font-family: "Poppins", sans-serif;
  }
  .sheet {
    position: relative;
    width: 1200px;
    height: 1200px;
  }
  .card {
    position: absolute;
    left: 150px;
    width: 900px;
    height: 514px;
    box-shadow: 0 14px 40px rgba(0,0,0,0.55);
  }
  .card--front { top: 60px; background: var(--card-dark); }
  .card--back  { top: 626px; background: var(--card-light); }
  .card__frame {
    position: absolute;
    inset: 0;
    width: 100%;
    height: 100%;
  }
  .card--front .card__frame { stroke: var(--frame-on-dark); }
  .card--back .card__frame { stroke: var(--frame-on-light); }
  .card__content {
    position: absolute;
    inset: 0;
    display: flex;
    flex-direction: column;
    align-items: center;
    justify-content: center;
    text-align: center;
  }
  .brand {
    display: flex;
    align-items: center;
    gap: 22px;
  }
  .brand__mark {
    width: 54px;
    height: 54px;
    border: 4px solid var(--gold);
  }
  .brand__name {
    font-weight: 500;
    font-size: 58px;
    letter-spacing: 1px;
    color: var(--gold);
    line-height: 1;
  }
  .card--back .brand__mark { border-color: var(--ink); width: 42px; height: 42px; border-width: 3px; }
  .card--back .brand__name { color: var(--ink); font-size: 44px; }
  .person {
    margin-top: 34px;
  }
  .person__name {
    font-weight: 700;
    font-size: 30px;
    color: var(--ink);
    line-height: 1.1;
  }
  .person__role {
    font-weight: 400;
    font-size: 20px;
    color: var(--gold);
    line-height: 1.2;
  }
  .contacts {
    margin-top: 26px;
    list-style: none;
    display: flex;
    flex-direction: column;
    align-items: center;
    gap: 4px;
  }
  .contacts__item {
    display: flex;
    align-items: center;
    gap: 10px;
    font-size: 22px;
    color: var(--ink);
    line-height: 1.3;
  }
  .contacts__icon {
    width: 18px;
    height: 18px;
    fill: var(--gold);
    flex: none;
  }
  .contacts__square {
    width: 16px;
    height: 16px;
    background: var(--gold);
    border-radius: 3px;
    flex: none;
  }
</style>
</head>
<body>
<main class="sheet">

  <section class="card card--front" aria-label="Card front">
    <svg class="card__frame" viewBox="0 0 900 514" fill="none" aria-hidden="true">
      <path stroke-width="2.5" d="M52 20 H848 A32 32 0 0 0 880 52 V462 A32 32 0 0 0 848 494 H52 A32 32 0 0 0 20 462 V52 A32 32 0 0 0 52 20 Z"/>
      <path stroke-width="1.5" d="M54 30 H846 A24 24 0 0 0 870 54 V460 A24 24 0 0 0 846 484 H54 A24 24 0 0 0 30 460 V54 A24 24 0 0 0 54 30 Z"/>
    </svg>
    <div class="card__content">
      <div class="brand">
        <span class="brand__mark"></span>
        <span class="brand__name">Torvane Cabinets</span>
      </div>
    </div>
  </section>

  <section class="card card--back" aria-label="Card back">
    <svg class="card__frame" viewBox="0 0 900 514" fill="none" aria-hidden="true">
      <path stroke-width="2.5" d="M52 20 H848 A32 32 0 0 0 880 52 V462 A32 32 0 0 0 848 494 H52 A32 32 0 0 0 20 462 V52 A32 32 0 0 0 52 20 Z"/>
      <path stroke-width="1.5" d="M54 30 H846 A24 24 0 0 0 870 54 V460 A24 24 0 0 0 846 484 H54 A24 24 0 0 0 30 460 V54 A24 24 0 0 0 54 30 Z"/>
    </svg>
    <div class="card__content">
      <div class="brand">
        <span class="brand__mark"></span>
        <span class="brand__name">Torvane Cabinets</span>
      </div>
      <div class="person">
        <p class="person__name">Miles Harwick</p>
        <p class="person__role">Craftsman</p>
      </div>
      <ul class="contacts">
        <li class="contacts__item">
          <svg class="contacts__icon" viewBox="0 0 24 24" aria-hidden="true"><path d="M6.6 10.8a15.5 15.5 0 0 0 6.6 6.6l2.2-2.2a1 1 0 0 1 1-.25 11.4 11.4 0 0 0 3.6.57 1 1 0 0 1 1 1V20a1 1 0 0 1-1 1A17 17 0 0 1 3 4a1 1 0 0 1 1-1h3.5a1 1 0 0 1 1 1c0 1.25.2 2.45.57 3.6a1 1 0 0 1-.25 1z"/></svg>
          <span>(123) 555-0147</span>
        </li>
        <li class="contacts__item">
          <svg class="contacts__icon" viewBox="0 0 24 24" aria-hidden="true"><path d="M2 5h20v14H2z M3.5 6.5 12 13l8.5-6.5" fill="none" stroke="var(--gold)" stroke-width="0"/><path d="M2 5h20v1.2L12 13 2 6.2z"/><path d="M2 8.3 12 15l10-6.7V19H2z"/></svg>
          <span>info@torvanecabinets.com.au</span>
        </li>
        <li class="contacts__item">
          <span class="contacts__square"></span>
          <span>@torvane.cabinets</span>
        </li>
      </ul>
    </div>
  </section>

</main>
</body>
</html>
```